Powerful crowd generating flyer to be built

What we are looking for is a cleverly worded flyer with a sophisticated graphic design. Our objective is to generate inquires and represent our brand.

Who we are: We a boutique gym in the Eastern Suburbs of Sydney. Up market, designer space, superior customer service and the very latest equipment. Our gym is like no other, innovative equipment from rock climbing wall, grindrig frames, QLM, sprint track, innovative classes never seen before in Sydney. Please refer to "Brightmoor Studio" (www.brightmoorstudio.com.au) "Mova hub" (www.movahub.com.au) and "Zentri" (www.zentri.com.au) for like for like gyms to gain a feeling on who we are.. We are: www.larkvalehealthclub.com.au (Please refer to this website for further photos)

Some of the services which need to be mentioned
1) Free Creche
2) Sydney most innovative classes
3) Sydney's best personal trainers
4) Free Parking

The OFFER: No Joining Fee, one month free membership (T&C apply) Limited space on offer, and only valid until 30.11.13

We are a cool looking gym, so we need a flyer which is slightly edgy, sophisticated and sleek.

Target Market(s)

60:40 Female to Male.
20 to 45 years old
Professionals and Mothers
Up market, wealthy, discerning

Industry/Entity Type

Boutique

Requirements
Must have
• The Flyer must be double sided, use a combination ofcthe photos attached,
Should not have
• cheese, generic, classic gym looking flyer

```html
<!DOCTYPE html>
<html lang="en">
<head>
<meta charset="utf-8">
<title>Larkvale Health Club – No Joining Fee Flyer</title>
<link rel="stylesheet" href="https://fonts.googleapis.com/css2?family=Exo+2:wght@400;500;600&display=swap">
<style>
  :root {
    --page-bg: #ececec;
    --lime: #a6de1e;
    --lime-light: #c7ec6e;
    --lime-pale: #dff3b0;
    --green: #6fb71a;
    --green-deep: #4f9a12;
    --grey: #9c9c9c;
    --grey-light: #c9c9c9;
    --offer-blue: #3aa6dc;
    --ink: #1f3a0c;
    --white: #ffffff;
  }
  * { margin: 0; padding: 0; box-sizing: border-box; }
  html, body {
    width: 1200px; height: 848px; overflow: hidden;
    background: var(--page-bg);
    font-family: "Exo 2", sans-serif;
  }
  .flyer {
    position: absolute; left: 370px; top: 91px;
    width: 460px; height: 666px;
    overflow: hidden; background: var(--lime-light);
  }
  .flyer__photo {
    position: absolute; left: 0; top: 0; width: 460px; height: 440px;
    background:
      linear-gradient(160deg, rgba(255,255,255,.0) 40%, rgba(200,90,50,.35) 70%, rgba(110,170,50,.5) 100%),
      linear-gradient(100deg, #6b4a30 0%, #7fae4a 28%, #d9dcd6 55%, #f2f2ee 80%, #c9c4b6 100%);
  }
  .flyer__shapes { position: absolute; inset: 0; }
  .flyer__url {
    position: absolute; left: 42px; top: 74px;
    color: var(--white); font-size: 13px; font-weight: 400; letter-spacing: .3px;
    transform: rotate(-21deg); transform-origin: left center;
  }
  .offer {
    position: absolute; left: 138px; top: 400px; width: 300px;
    text-align: center; text-transform: uppercase; line-height: 1.05;
    transform: rotate(-18deg); transform-origin: center;
  }
  .offer__headline { color: var(--offer-blue); font-size: 33px; font-weight: 500; }
  .offer__detail { color: var(--ink); font-size: 15.5px; font-weight: 600; margin-top: 2px; }
  .offer__date { color: var(--offer-blue); font-size: 50px; font-weight: 600; margin-top: 2px; }
</style>
</head>
<body>
  <main class="flyer">
    <div class="flyer__photo" role="img" aria-label="Photo of the gym interior: climbing wall, rope net, turf training zone, orange sprint track, palms and weights floor"></div>

    <svg class="flyer__shapes" width="460" height="666" viewBox="0 0 460 666" aria-hidden="true">
      <!-- header facets -->
      <polygon points="0,0 285,0 258,60 110,145 0,105" fill="var(--green)"/>
      <polygon points="0,0 185,0 120,55 0,70" fill="var(--lime)" opacity=".85"/>
      <polygon points="120,55 285,0 258,60" fill="var(--green-deep)" opacity=".6"/>
      <!-- photo frame line -->
      <polyline points="222,170 370,150 365,160 460,150" fill="none" stroke="var(--white)" stroke-width="3"/>
      <!-- lower panel -->
      <polygon points="0,424 460,352 460,666 0,666" fill="var(--lime-light)"/>
      <polygon points="0,424 460,352 460,378 160,430" fill="var(--green)"/>
      <polygon points="0,424 160,430 95,560 0,530" fill="var(--green-deep)"/>
      <polygon points="0,530 95,560 0,650" fill="var(--lime)"/>
      <polygon points="0,650 95,560 180,666 0,666" fill="var(--green)"/>
      <polygon points="95,560 280,600 180,666" fill="var(--lime-pale)"/>
      <polygon points="160,430 460,378 400,460" fill="var(--lime-light)" opacity=".8"/>
      <!-- grey facets -->
      <polygon points="410,470 460,440 460,560" fill="var(--grey-light)"/>
      <polygon points="380,580 460,560 460,666 300,666" fill="var(--grey)"/>
      <polygon points="230,666 330,600 380,580 300,666" fill="var(--white)"/>
    </svg>

    <p class="flyer__url">www.larkvalehealthclub.com.au</p>

    <section class="offer">
      <h1 class="offer__headline">No Joining Fee</h1>
      <p class="offer__detail">One month free membership<br>(T&amp;C apply)<br>Limited space on offer,<br>and only valid until</p>
      <p class="offer__date">30.11.13</p>
    </section>
  </main>
</body>
</html>
```